Mabel's Fitness Business Cards

I would like my business cards to look expensive and sophisticated using my logo and the information below.

FRONT
Mabel’s Fitness logo

Tag line Become your happiest, healthiest and strongest self

Mabel Quint Harlow
Personal Trainer

e. mabel@mabelsfitstudio.example

t. 0781530462

w. www.mabelsfitstudio.example

```html
<!DOCTYPE html>
<html lang="en">
<head>
<meta charset="utf-8">
<title>Mabel's Fitness – Business Cards</title>
<link href="https://fonts.googleapis.com/css2?family=Lato:ital,wght@0,400;0,700;1,400&display=swap" rel="stylesheet">
<style>
  :root {
    --teal: #69b4bc;
    --teal-deep: #5aa8b1;
    --mauve: #a48f8d;
    --white: #ffffff;
    --backdrop: #ece9e7;
  }
  * { margin: 0; padding: 0; box-sizing: border-box; }
  html, body { width: 1200px; height: 900px; overflow: hidden; }
  body {
    background: var(--backdrop);
    font-family: "Lato", sans-serif;
    position: relative;
  }
  .card {
    position: absolute;
    overflow: hidden;
    box-shadow: 0 6px 18px rgba(0,0,0,0.12);
  }

  /* Front card */
  .card--front {
    left: 178px; top: 73px;
    width: 588px; height: 364px;
    background: var(--teal);
  }
  .front-disc {
    position: absolute;
    left: -18px; top: -2px;
    width: 348px; height: 348px;
    border-radius: 50%;
    background: var(--mauve);
    display: flex; align-items: center; justify-content: center;
  }
  .front-disc__name {
    color: var(--white);
    font-weight: 400;
    font-size: 26px;
    letter-spacing: 3px;
    text-transform: uppercase;
    text-align: center;
    line-height: 1.4;
  }
  .trainer {
    position: absolute;
    right: 26px; top: 48px;
    text-align: right;
    color: var(--white);
  }
  .trainer__name { font-weight: 700; font-size: 19px; letter-spacing: 0.3px; text-transform: uppercase; }
  .trainer__role { font-weight: 400; font-size: 16px; margin-top: 2px; }
  .contacts {
    position: absolute;
    right: 26px; top: 203px;
    list-style: none;
    color: var(--white);
    font-size: 16px;
  }
  .contacts li {
    display: flex; align-items: center; justify-content: flex-end;
    gap: 3px; height: 21px;
  }
  .contacts svg { width: 19px; height: 19px; flex: none; }
  .tagline {
    position: absolute;
    right: 26px; top: 285px;
    text-align: right;
    color: var(--white);
    font-style: italic;
    font-size: 14px;
    line-height: 19px;
    text-transform: uppercase;
  }

  /* Back card */
  .card--back {
    left: 388px; top: 505px;
    width: 567px; height: 352px;
    background: var(--white);
  }
  .back-mark {
    position: absolute;
    left: 0; right: 0; top: 82px;
    display: flex; flex-direction: column; align-items: center;
  }
  .back-mark__disc {
    width: 104px; height: 104px;
    border-radius: 50%;
    background: var(--mauve);
  }
  .back-mark__name {
    margin-top: 34px;
    color: var(--teal-deep);
    font-weight: 400;
    font-size: 28px;
    letter-spacing: 7px;
    text-transform: uppercase;
  }
  .back-web {
    position: absolute;
    left: 0; right: 0; top: 297px;
    text-align: center;
    color: var(--mauve);
    font-size: 15px;
    letter-spacing: 1.6px;
    text-transform: uppercase;
  }
</style>
</head>
<body>

<section class="card card--front">
  <div class="front-disc">
    <span class="front-disc__name">Mabel’s<br>Fitness</span>
  </div>

  <div class="trainer">
    <p class="trainer__name">Mabel Quint Harlow</p>
    <p class="trainer__role">Personal Trainer</p>
  </div>

  <ul class="contacts">
    <li>0781530462
      <svg viewBox="0 0 20 20" aria-hidden="true"><circle cx="10" cy="10" r="9" fill="var(--white)"/><path d="M6.5 8.5h7l1 3h-9z M8 8.5v-1.5h4v1.5" fill="var(--teal)"/></svg>
    </li>
    <li>mabel@mabelsfitstudio.example
      <svg viewBox="0 0 20 20" aria-hidden="true"><circle cx="10" cy="10" r="9" fill="var(--white)"/><rect x="5.5" y="6.8" width="9" height="6.4" fill="var(--teal)"/><path d="M5.5 7l4.5 3.6L14.5 7" fill="none" stroke="var(--white)" stroke-width="1"/></svg>
    </li>
    <li>www.mabelsfitstudio.example
      <svg viewBox="0 0 20 20" aria-hidden="true"><circle cx="10" cy="10" r="9" fill="var(--white)"/><circle cx="10" cy="10" r="5" fill="var(--teal)"/><path d="M5 10h10M10 5c-2 3-2 7 0 10M10 5c2 3 2 7 0 10" fill="none" stroke="var(--white)" stroke-width="0.8"/></svg>
    </li>
  </ul>

  <p class="tagline">Become your happiest<br>healthiest and strongest self</p>
</section>

<section class="card card--back">
  <div class="back-mark">
    <div class="back-mark__disc"></div>
    <p class="back-mark__name">Mabel’s Fitness</p>
  </div>
  <p class="back-web">www.mabelsfitstudio.example</p>
</section>

</body>
</html>
```